Business Card Design Project

We need a business card design for a company based in San Francisco called PlanGlide. PlanGlide makes customized academic planners for high schools and middle schools. Currently we sell directly to the schools who either re-sell or give the planners to their students. The planners are designed to help students stay organized and manage their time. The books are unique in that they are made individually for each school and include the school's events, student artwork and most importantly the daily class schedule in each week. This helps the student to understand what classes they have each day and what homework they need to do each night.

Currently the product is B:B; however, we are exploring ways in which to make this a B:C. Please review website at www.planglide.net

The final design should communicate time management and organization.

Card should be one-sided

Information for the business card should include

Dorothy Kellner Voss
Founder
dorothy@planglide.net
415-836-1752

Target Market(s)

High school and middle school administrators

Industry/Entity Type

School

Requirements
Must have
• One sided design
Nice to have
• I'm open to new interpretations of the logo as well as color usage. I'm also open to changing the font of the logo type.
Should not have
• Please use a san serif font.

```html
<!DOCTYPE html>
<html lang="en">
<head>
<meta charset="utf-8">
<title>PlanGlide Business Card</title>
<link rel="stylesheet" href="https://fonts.googleapis.com/css2?family=Fira+Sans:wght@400;600&display=swap">
<style>
  :root {
    --backdrop: #1c1c1c;
    --card: #ffffff;
    --ink: #111111;
    --muted: #555555;
    --band: #000000;
  }
  html, body {
    margin: 0;
    padding: 0;
    width: 1200px;
    height: 900px;
    overflow: hidden;
    background: var(--backdrop);
    font-family: "Fira Sans", sans-serif;
  }
  .card {
    position: absolute;
    left: 180px;
    top: 210px;
    width: 840px;
    height: 480px;
    background: var(--card);
    color: var(--ink);
    overflow: hidden;
    box-shadow: 0 10px 30px rgba(0,0,0,0.5);
  }
  .brand {
    position: absolute;
    left: 56px;
    top: 96px;
  }
  .brand-name {
    font-size: 50px;
    font-weight: 400;
    line-height: 1;
    letter-spacing: -0.5px;
  }
  .brand-tagline {
    margin-top: 6px;
    font-size: 18px;
    letter-spacing: 0.3px;
  }
  .band {
    position: absolute;
    left: 0;
    top: 196px;
    width: 480px;
    height: 30px;
    background: var(--band);
    clip-path: polygon(0 0, 100% 0, 96% 100%, 0 100%);
  }
  .person {
    position: absolute;
    left: 496px;
    top: 176px;
  }
  .person-name {
    font-size: 22px;
    font-weight: 600;
  }
  .person-title {
    margin-top: 4px;
    margin-left: 18px;
    font-size: 17px;
    color: var(--muted);
  }
  .address {
    position: absolute;
    left: 64px;
    top: 280px;
    font-size: 18px;
    line-height: 1.4;
  }
  .contacts {
    position: absolute;
    left: 64px;
    top: 358px;
    margin: 0;
    padding: 0;
    list-style: none;
    font-size: 22px;
  }
  .contacts li {
    display: flex;
    align-items: center;
    gap: 12px;
    height: 34px;
  }
  .contacts svg {
    width: 24px;
    height: 24px;
  }
</style>
</head>
<body>
  <section class="card">
    <div class="brand">
      <div class="brand-name">PlanGlide</div>
      <div class="brand-tagline">Customized Academic Planners</div>
    </div>

    <div class="band"></div>

    <div class="person">
      <div class="person-name">Dorothy Kellner Voss</div>
      <div class="person-title">Founder</div>
    </div>

    <div class="address">
      418 Alder Street, Suite 210<br>
      San Francisco
    </div>

    <ul class="contacts">
      <li>
        <svg viewBox="0 0 24 24" aria-hidden="true">
          <circle cx="12" cy="12" r="11" fill="none" stroke="#111" stroke-width="1.6"/>
          <path d="M8.2 6.5l2 2.4-1.2 1.4c.8 1.7 2 2.9 3.7 3.7l1.4-1.2 2.4 2-1.1 1.8c-3.9-.5-7.2-3.8-7.7-7.7z" fill="#111"/>
        </svg>
        415-836-1752
      </li>
      <li>
        <svg viewBox="0 0 24 24" aria-hidden="true">
          <rect x="2" y="6" width="20" height="13" fill="#111"/>
          <path d="M2 6l10 8 10-8" fill="none" stroke="#fff" stroke-width="1.5"/>
        </svg>
        dorothy@planglide.net
      </li>
      <li>
        <svg viewBox="0 0 24 24" aria-hidden="true">
          <circle cx="12" cy="12" r="10" fill="none" stroke="#111" stroke-width="1.6"/>
          <ellipse cx="12" cy="12" rx="4.5" ry="10" fill="none" stroke="#111" stroke-width="1.4"/>
          <path d="M2 12h20M4 7h16M4 17h16" stroke="#111" stroke-width="1.4"/>
        </svg>
        www.planglide.net
      </li>
    </ul>
  </section>
</body>
</html>
```